IT Services company general flyer

Looking for a printable US letter size flyer to give a brief overview of the services we offer. We also partner with another company for their services as well. Please check out our website at www.gearbymarlon.com and click on "Our Services" to learn about our services and visit www.bluepinesafety,com and click on services to learn about their services. Several of our services do overlap, so they only need to be on the flyer once. Let me know if this is too much content and we need to weed some out. We do not want Home phone service on this flyer. The basic design of the flyer should mimic similar to the VOIP one you did for me for the colors and logo. Also check out the "Who Choose us" page on www.gearbymarlon.com to include some of that as well.
Updates

Gathering more feedback

Target Market(s)

Targeting Small businesses that may not normally have a budget for their IT Services

Industry/Entity Type

It Service

Font styles to use
Serif
Sans Serif

Requirements
Must have
• Must include my logo, phone number and email/website address and must follow the same basic template of my previous flyers.

```html
<!DOCTYPE html>
<html lang="en">
<head>
<meta charset="utf-8">
<title>Gear By Marlon – IT Services Flyer</title>
<link href="https://fonts.googleapis.com/css2?family=Open+Sans:wght@300;400;600;700;800&family=Montserrat:wght@800;900&display=swap" rel="stylesheet">
<style>
:root{
  --red:#7a1c1e;
  --red-deep:#4f1012;
  --navy:#1f2a4f;
  --gray-tab:#8d8f94;
  --ink:#3d3d3d;
  --white:#ffffff;
  --page:#eeeff1;
}
*{box-sizing:border-box;margin:0;padding:0}
html,body{width:1101px;height:1200px;overflow:hidden;background:var(--page);font-family:"Open Sans",Arial,sans-serif}
.flyer{position:absolute;left:90px;top:6px;width:920px;height:1188px;background:var(--white);overflow:hidden;box-shadow:0 6px 20px rgba(0,0,0,.18)}
.abs{position:absolute}

/* header */
.brand-partner{position:absolute;left:48px;top:40px;display:flex;align-items:center;gap:10px;color:var(--red);font-size:27px;font-weight:800;letter-spacing:.5px}
.brand-partner .mark{width:30px;height:30px;background:var(--red)}
.brand-main-mark{position:absolute;left:566px;top:22px;width:80px;height:80px;border-radius:50%;background:var(--navy)}
.brand-divider{position:absolute;left:659px;top:12px;width:1px;height:110px;background:#cfd0d4}
.brand-main{position:absolute;left:672px;top:28px;color:var(--navy);font-size:30px;font-weight:800;line-height:34px;letter-spacing:.5px}

.headline{position:absolute;left:0;width:920px;top:172px;text-align:center;font-size:48px;font-weight:300;color:#2f2f33;letter-spacing:-.5px}
.headline strong{font-weight:800;color:var(--red)}
.intro{position:absolute;left:55px;width:810px;top:254px;text-align:center;font-size:17px;line-height:23px;color:var(--ink)}

/* services */
.services-bg{position:absolute;left:0;top:360px;width:920px;height:735px}
.servers{position:absolute;left:0;top:793px;width:920px;height:302px;background:linear-gradient(100deg,rgba(255,255,255,0) 0%,rgba(150,152,158,.22) 50%,rgba(255,255,255,0) 100%)}
.services-tab{position:absolute;left:308px;top:366px;width:314px;height:52px;text-align:center;color:var(--white);font-weight:800;font-size:28px;line-height:52px;letter-spacing:.5px}
.col-head{position:absolute;color:var(--white);font-weight:800;font-size:31px;display:flex;align-items:center;gap:14px;height:44px}
.col-head .rule{height:2px;background:var(--white)}
.service-list{position:absolute;list-style:none}
.service-list li{display:flex;align-items:center;gap:10px;height:50px;color:var(--white);font-weight:600;font-size:13.5px;letter-spacing:.1px;white-space:nowrap}
.service-list svg{flex:none}
.portrait{position:absolute;left:650px;top:394px;width:270px;height:410px;background:radial-gradient(ellipse at 55% 35%,#9a9aa6 0%,#6f7282 45%,rgba(90,30,35,0) 78%)}

/* features */
.feature{position:absolute;top:835px;width:200px;text-align:center}
.feature .icon{height:62px;display:flex;justify-content:center;align-items:center}
.feature h3{font-family:"Montserrat",Arial,sans-serif;font-weight:900;color:var(--red);font-size:17px;line-height:29px;margin-top:6px;min-height:58px}
.feature p{text-align:justify;font-size:13.5px;line-height:20px;color:#2f2f2f;margin-top:10px}

/* footer */
.visit{position:absolute;left:28px;top:1109px;color:var(--white);font-size:13px;display:flex;align-items:center;gap:10px}
.visit .social{width:16px;height:16px;background:var(--white);border-radius:3px}
.site{position:absolute;left:27px;top:1138px;color:var(--white);font-size:24px;letter-spacing:2px}
.contact-tab{position:absolute;left:438px;top:1101px;width:175px;height:30px;color:var(--white);font-size:21px;line-height:30px;text-align:center}
.phone{position:absolute;left:650px;top:1096px;color:var(--white);font-weight:800;font-size:32px;display:flex;align-items:center;gap:8px}
.email{position:absolute;left:650px;top:1143px;color:var(--white);font-size:17px;display:flex;align-items:center;gap:14px}
</style>
</head>
<body>
<main class="flyer">

  <header>
    <div class="brand-partner"><span class="mark"></span>BLUEPINE SAFETY</div>
    <div class="brand-main-mark"></div>
    <div class="brand-divider"></div>
    <div class="brand-main">GEAR<br>BY MARLON</div>
  </header>

  <h1 class="headline"><strong>IT support,</strong> to all systems and all size</h1>
  <p class="intro">Talk to us today and get the best IT support that's right for your business and let our team of qualified and certified nationally of Gear By Marlon engineers help you with your business computer network, software or computer systems.</p>

  <svg class="services-bg" viewBox="0 0 920 735" aria-hidden="true">
    <defs>
      <linearGradient id="bandShade" x1="0" y1="0" x2="1" y2="1">
        <stop offset="0" stop-color="#8a2326"/>
        <stop offset=".5" stop-color="#6d181b"/>
        <stop offset="1" stop-color="#4a0f11"/>
      </linearGradient>
      <linearGradient id="grayShade" x1="0" y1="0" x2="1" y2="0">
        <stop offset="0" stop-color="#cfd0d3"/>
        <stop offset=".5" stop-color="#e2e2e4"/>
        <stop offset="1" stop-color="#c9cacd"/>
      </linearGradient>
    </defs>
    <path d="M0 400 H920 V735 H0Z" fill="url(#grayShade)"/>
    <path d="M0 58 H920 V447 Q700 452 470 466 Q240 450 0 433Z" fill="url(#bandShade)"/>
    <path d="M308 58 L320 14 Q324 6 334 6 H596 Q606 6 610 14 L622 58Z" fill="var(--red-deep)"/>
  </svg>
  <div class="servers" role="img" aria-label="Faint photo of server hardware behind the feature columns"></div>
  <div class="services-tab">OUR SERVICES</div>

  <div class="col-head" style="left:22px;top:437px">
    <span class="rule" style="width:28px"></span>
    <svg width="40" height="42" viewBox="0 0 40 42"><ellipse cx="20" cy="7" rx="18" ry="6" fill="#fff"/><path d="M2 12 Q20 22 38 12 V20 Q20 30 2 20Z M2 24 Q20 34 38 24 V32 Q20 42 2 32Z" fill="#fff"/></svg>
    <span>DATA</span>
  </div>
  <svg class="abs" style="left:218px;top:458px" width="160" height="40" aria-hidden="true"><path d="M0 1 H85 V38" fill="none" stroke="#fff" stroke-width="2"/><path d="M140 38 V1 H147" fill="none" stroke="#fff" stroke-width="2"/></svg>

  <div class="col-head" style="left:380px;top:437px">
    <svg width="50" height="36" viewBox="0 0 50 36"><path d="M12 34 A11 11 0 0 1 11 12 A13 13 0 0 1 35 9 A12 12 0 0 1 40 34Z" fill="#fff"/></svg>
    <span>CLOUD</span>
    <span class="rule" style="width:48px"></span>
  </div>

  <ul class="service-list" style="left:15px;top:488px">
    <li><svg width="38" height="38"><circle cx="19" cy="19" r="17" fill="none" stroke="#fff" stroke-width="1.6"/><path d="M19 9 L27 12 V19 Q27 26 19 29 Q11 26 11 19 V12Z" fill="none" stroke="#fff" stroke-width="1.6"/></svg>MANAGED SECURITY SERVICES</li>
    <li><svg width="38" height="38"><circle cx="19" cy="19" r="17" fill="none" stroke="#fff" stroke-width="1.6"/><circle cx="19" cy="19" r="3" fill="#fff"/><circle cx="11" cy="12" r="2.5" fill="#fff"/><circle cx="27" cy="12" r="2.5" fill="#fff"/><circle cx="11" cy="26" r="2.5" fill="#fff"/><circle cx="27" cy="26" r="2.5" fill="#fff"/><path d="M11 12 L27 26 M27 12 L11 26" stroke="#fff"/></svg>NETWORK &amp; WIRELESS CYBER SECURITY</li>
    <li><svg width="38" height="38"><circle cx="19" cy="19" r="17" fill="none" stroke="#fff" stroke-width="1.6"/><rect x="10" y="12" width="12" height="4" fill="#fff"/><rect x="10" y="18" width="12" height="4" fill="#fff"/><rect x="10" y="24" width="12" height="4" fill="#fff"/><circle cx="26" cy="16" r="3.5" fill="#fff"/></svg>MANAGED IT SERVICES</li>
    <li><svg width="38" height="38"><circle cx="19" cy="19" r="17" fill="none" stroke="#fff" stroke-width="1.6"/><rect x="11" y="10" width="13" height="17" fill="none" stroke="#fff" stroke-width="1.5"/><circle cx="22" cy="22" r="5" fill="none" stroke="#fff" stroke-width="1.5"/><path d="M20 22 L22 24 L25 20" stroke="#fff" fill="none"/></svg>SECURITY ASSESSMENT SERVICES</li>
    <li><svg width="38" height="38"><circle cx="19" cy="19" r="17" fill="none" stroke="#fff" stroke-width="1.6"/><rect x="10" y="11" width="16" height="5" fill="none" stroke="#fff" stroke-width="1.5"/><rect x="10" y="18" width="16" height="5" fill="none" stroke="#fff" stroke-width="1.5"/><circle cx="26" cy="26" r="4" fill="none" stroke="#fff" stroke-width="1.5"/></svg>BACKUP &amp; DISASTER RECOVERY SERVICES</li>
    <li><svg width="38" height="38"><circle cx="19" cy="19" r="17" fill="none" stroke="#fff" stroke-width="1.6"/><path d="M19 8 L28 12 V19 Q28 27 19 30 Q10 27 10 19 V12Z" fill="none" stroke="#fff" stroke-width="1.6"/><circle cx="19" cy="19" r="3.5" fill="#fff"/></svg>RANSOMWARE &amp; THREAT RESPONSE SERVICES</li>
  </ul>

  <ul class="service-list" style="left:371px;top:488px">
    <li><svg width="46" height="38"><path d="M10 32 A9 9 0 0 1 9 15 A12 12 0 0 1 32 12 A10 10 0 0 1 36 32Z" fill="none" stroke="#fff" stroke-width="1.6"/><rect x="18" y="16" width="8" height="8" fill="none" stroke="#fff" stroke-width="1.4"/></svg>BUSINESS OFFICE SUITE SERVICES</li>
    <li><svg width="46" height="38"><path d="M10 32 A9 9 0 0 1 9 15 A12 12 0 0 1 32 12 A10 10 0 0 1 36 32Z" fill="none" stroke="#fff" stroke-width="1.6"/><rect x="25" y="24" width="10" height="9" rx="1" fill="#fff"/><path d="M27 24 V21 A3 3 0 0 1 33 21 V24" fill="none" stroke="#fff" stroke-width="1.5"/></svg>ENDPOINT SECURITY SERVICES</li>
    <li><svg width="46" height="38"><path d="M14 24 A8 8 0 0 1 13 9 A10 10 0 0 1 32 8 A8 8 0 0 1 34 24Z" fill="none" stroke="#fff" stroke-width="1.6"/><path d="M23 24 V34 M16 28 V34 M30 28 V34" stroke="#fff" stroke-width="1.6"/></svg>CLOUD SERVICES COMPUTING</li>
    <li><svg width="46" height="38"><path d="M12 22 A8 8 0 0 1 11 7 A10 10 0 0 1 32 6 A8 8 0 0 1 34 22Z" fill="none" stroke="#fff" stroke-width="1.6"/><rect x="16" y="14" width="14" height="10" fill="none" stroke="#fff" stroke-width="1.5"/><path d="M23 24 V30 M14 34 H32 M14 30 H32" stroke="#fff" stroke-width="1.5"/></svg>HOSTED CLOUD DESKTOP</li>
    <li><svg width="46" height="38"><path d="M12 26 A9 9 0 0 1 11 9 A12 12 0 0 1 34 8 A9 9 0 0 1 36 26Z" fill="none" stroke="#fff" stroke-width="1.6"/><path d="M18 12 Q16 20 24 23 L27 20 L24 17 L22 18 Q20 16 21 14 L19 11Z" fill="#fff"/><path d="M23 26 V34" stroke="#fff" stroke-width="1.6"/></svg>CLOUD TELEPHONE SYSTEM</li>
  </ul>

  <div class="portrait" role="img" aria-label="Photo of a smiling businesswoman in a gray suit celebrating"></div>

  <section class="feature" style="left:21px">
    <div class="icon"><svg width="64" height="62" viewBox="0 0 64 62" aria-hidden="true"><circle cx="32" cy="31" r="28" fill="none" stroke="#111" stroke-width="3"/><path d="M6 31 Q32 8 58 31 Q32 54 6 31Z" fill="none" stroke="#111" stroke-width="3"/><circle cx="32" cy="31" r="10" fill="#111"/><rect x="27" y="27" width="10" height="7" fill="#fff"/></svg></div>
    <h3>Proactive Monitoring<br>and Management</h3>
    <p>We continuously monitor and manage your entire technology infrastructure to ensure consistent up time and availability</p>
  </section>
  <section class="feature" style="left:247px">
    <div class="icon"><svg width="64" height="62" viewBox="0 0 64 62" aria-hidden="true"><rect x="30" y="4" width="30" height="24" fill="none" stroke="#111" stroke-width="2.5"/><path d="M35 11 H55 M35 17 H55 M35 23 H48" stroke="#111" stroke-width="2"/><circle cx="22" cy="26" r="9" fill="none" stroke="#111" stroke-width="2.5"/><path d="M11 26 A11 11 0 0 1 33 26" fill="none" stroke="#111" stroke-width="3"/><path d="M6 58 Q6 40 22 40 Q38 40 38 58Z" fill="#111"/></svg></div>
    <h3>Remote Technical<br>Support</h3>
    <p>Fast, effective remote technical support to resolve issues and return you to being productive</p>
  </section>
  <section class="feature" style="left:472px">
    <div class="icon"><svg width="90" height="62" viewBox="0 0 90 62" aria-hidden="true"><g fill="none" stroke="#111" stroke-width="2.5"><circle cx="20" cy="22" r="8"/><circle cx="70" cy="22" r="8"/><circle cx="45" cy="18" r="9"/><path d="M4 52 Q4 34 20 34 Q28 34 31 38"/><path d="M86 52 Q86 34 70 34 Q62 34 59 38"/><path d="M27 56 Q27 32 45 32 Q63 32 63 56Z"/></g></svg></div>
    <h3>vCIO</h3>
    <p>Coordinated strategy planning for projects, budgeting, hardware life-cycling and 3rd party vendor coordination</p>
  </section>
  <section class="feature" style="left:697px">
    <div class="icon"><svg width="76" height="62" viewBox="0 0 76 62" aria-hidden="true"><g fill="none" stroke="#111" stroke-width="2.5"><circle cx="38" cy="31" r="14" stroke-dasharray="4 3"/><path d="M6 52 H22 L34 46 H46"/><path d="M70 10 H54 L42 16 H30"/></g><text x="38" y="37" text-anchor="middle" font-family="Open Sans, sans-serif" font-weight="800" font-size="17" fill="#111">$</text></svg></div>
    <h3>Predictable<br>Budgeting</h3>
    <p>When you work with us, you have one, flat rate for your technology spend each month. So, there are no surprise bills or hourly charges to dispute.</p>
  </section>

  <svg class="abs" style="left:0;top:1095px" width="920" height="93" aria-hidden="true">
    <path d="M0 0 H225 L250 29 H0Z" fill="var(--navy)"/>
    <path d="M0 29 H600 L565 93 H0Z" fill="var(--red)"/>
    <path d="M446 6 H620 L606 35 H433Z" fill="var(--gray-tab)"/>
    <path d="M608 0 H920 V93 H565Z" fill="var(--navy)"/>
  </svg>
  <div class="visit">VISIT US AT <span class="social"></span></div>
  <div class="site">www.gearbymarlon.com</div>
  <div class="contact-tab">CONTACT US</div>
  <div class="phone"><svg width="28" height="28" viewBox="0 0 28 28" aria-hidden="true"><circle cx="14" cy="14" r="12" fill="none" stroke="#fff" stroke-width="2"/><path d="M9 8 Q8 17 18 20 L20 17 L17 15 L15 16 Q12 14 12 12 L13 10 L11 7Z" fill="#fff"/></svg>555.014.2276</div>
  <div class="email"><svg width="20" height="14" viewBox="0 0 20 14" aria-hidden="true"><rect width="20" height="14" fill="#fff"/><path d="M0 0 L10 8 L20 0" fill="none" stroke="var(--navy)" stroke-width="1.6"/></svg>sales@gearbymarlon.com</div>

</main>
</body>
</html>
```